Sophisticated, clean website reflecting my feminine, playful side to sell my abstract art,

I need a website no more than 3 pages to showcase my paintings, a little about me and some contact info. I do abstracts so looking for something a little edgy, yet feminine and current.
Updates

Hi there, These are some artists websites that I Iike: Mirabelvoss.com (I like how airy it is) tobiasmerrowind.com kevinplodderas.com (I like how it scrolls) I'll need a place for a photo ( a headshot-i do not have it yet so I'll need to be able to upload that later) as well as an area for my bio. Also, it's important that I will be able to upload any new photos and descriptions easily so it should be user friendly. Lastly, I like in a sunny place so would like to have this seem upbeat and playful as that is how i like to paint. thanks-I'm trying to upload my photos now -

Target Market(s)

ppl ages 35-70 who want large scale art for their homes

Industry/Entity Type

art

Coding

Coded - Design and coding required

Number of Pages Required

3 page

Colors

Designer to choose colors to be used in the design.

Requirements
Must have
• photos of my art, a place for my bio, be easy to reach me. tasteful-nothing too "in your face" -my clients are pretty high end and organized. They like clean lines
Nice to have
• sophisticated background, muted tones in the back-similar clean font throughout-no cursive
Should not have
• too many dark areas. Too many blocks of color. Too serious.

```html
<!DOCTYPE html>
<html lang="en">
<head>
<meta charset="UTF-8">
<title>Clara Wendt Art</title>
<link href="https://fonts.googleapis.com/css2?family=Oswald:wght@300;400&family=Baloo+Bhai+2:wght@400&display=swap" rel="stylesheet">
<style>
  :root {
    --ink: #111111;
    --rule: #6b6b6b;
    --paper: #ffffff;
    --wash-a: rgba(196, 214, 204, 0.22);
    --wash-b: rgba(230, 222, 200, 0.18);
    --art-deep: #1f7a4a;
    --art-green: #5aa83a;
    --art-teal: #1f8a80;
    --art-ochre: #d6b860;
    --art-blush: #e9e3e6;
    --portrait-bg: #dfe2e5;
    --portrait-shirt: #f4f4f4;
    --accent: #f2cf3b;
  }
  * { margin: 0; padding: 0; box-sizing: border-box; }
  html, body { width: 1040px; height: 1200px; overflow: hidden; background: var(--paper); }
  body { position: relative; color: var(--ink); font-family: "Baloo Bhai 2", sans-serif; }

  .backdrop-wash {
    position: absolute; left: 199px; top: 0; width: 653px; height: 760px;
    background:
      radial-gradient(ellipse at 30% 20%, var(--wash-a), transparent 60%),
      radial-gradient(ellipse at 70% 90%, var(--wash-b), transparent 60%),
      linear-gradient(180deg, rgba(220,230,224,0.18), rgba(255,255,255,0) 100%);
  }

  .site-header { position: absolute; left: 0; top: 0; width: 1040px; height: 150px; }
  .brand {
    position: absolute; left: 0; top: 22px; width: 1040px; height: 59px;
    display: flex; justify-content: center; align-items: center; gap: 11px;
    font-family: "Oswald", sans-serif; font-weight: 300; font-size: 12.5px;
    text-transform: uppercase; color: var(--ink);
  }
  .brand-square { width: 46px; height: 59px; background: var(--ink); }
  .brand-rule { position: absolute; left: 445px; top: 95px; width: 149px; height: 1px; background: var(--rule); }
  .main-nav {
    position: absolute; top: 116px; left: 0; width: 1040px;
    display: flex; justify-content: center; gap: 41px;
    font-family: "Oswald", sans-serif; font-weight: 300; font-size: 15px;
  }
  .main-nav a { color: var(--ink); text-decoration: none; }

  .hero-slider { position: absolute; left: 36px; top: 162px; width: 968px; height: 504px; }
  .hero-art {
    width: 100%; height: 100%;
    background:
      radial-gradient(ellipse at 35% 25%, var(--art-ochre) 0, transparent 22%),
      radial-gradient(ellipse at 80% 55%, var(--art-blush) 0, transparent 30%),
      radial-gradient(ellipse at 15% 70%, var(--art-teal) 0, transparent 35%),
      radial-gradient(ellipse at 60% 80%, var(--art-deep) 0, transparent 40%),
      linear-gradient(135deg, var(--art-deep), var(--art-green) 45%, var(--art-teal));
  }
  .slider-arrow { position: absolute; top: 237px; width: 18px; height: 30px; }
  .slider-arrow.prev { left: 22px; }
  .slider-arrow.next { left: 928px; }

  .about-portrait {
    position: absolute; left: 36px; top: 761px; width: 421px; height: 309px;
    border: 2px solid #222;
    background:
      radial-gradient(ellipse at 50% 95%, var(--portrait-shirt) 0, var(--portrait-shirt) 30%, transparent 31%),
      linear-gradient(180deg, #e7e9eb, var(--portrait-bg));
  }
  .about-bio {
    position: absolute; left: 478px; top: 808px; width: 354px;
    font-size: 12.2px; line-height: 18px; color: #222;
  }
  .signature-slot {
    position: absolute; left: 478px; top: 908px; width: 88px; height: 56px;
    background: #f1f1f1; border-radius: 3px;
  }

  .view-gallery {
    position: absolute; left: 191px; top: 1091px;
    display: flex; align-items: center; gap: 10px;
    font-family: "Oswald", sans-serif; font-weight: 400; font-size: 12.5px;
    color: var(--ink); text-decoration: none; text-transform: uppercase;
  }

  .site-footer {
    position: absolute; left: 0; top: 1172px; width: 1040px; text-align: center;
    font-size: 11px; color: #333;
  }
</style>
</head>
<body>
  <div class="backdrop-wash" aria-hidden="true"></div>

  <header class="site-header">
    <div class="brand"><span>Clara</span><span class="brand-square"></span><span>Wendt</span></div>
    <div class="brand-rule"></div>
    <nav class="main-nav">
      <a href="#">GALLERY</a>
      <a href="#">ABOUT</a>
      <a href="#">CONTACT</a>
    </nav>
  </header>

  <section class="hero-slider">
    <div class="hero-art" role="img" aria-label="Featured abstract painting in greens, teal and ochre brushstrokes"></div>
    <svg class="slider-arrow prev" viewBox="0 0 18 30" aria-label="Previous"><polyline points="15,3 3,15 15,27" fill="none" stroke="#111" stroke-width="3"/></svg>
    <svg class="slider-arrow next" viewBox="0 0 18 30" aria-label="Next"><polyline points="3,3 15,15 3,27" fill="none" stroke="#111" stroke-width="3"/></svg>
  </section>

  <div class="about-portrait" role="img" aria-label="Portrait photo of the artist against a light grey wall"></div>

  <p class="about-bio">Lorem ipsum dolor sit amet, consectetuer adipiscing elit. Aenean commodo ligula eget dolor. Aenean massa. Cum sociis natoque penatibus et magnis dis parturient montes, nascetur ridiculus mus. Donec quam felis, ultricies nec, pellentesque eu, pretium quis, sem. Nulla consequat massa quis enim.</p>
  <div class="signature-slot" role="img" aria-label="Artist's handwritten signature"></div>

  <a class="view-gallery" href="#">
    <span>View Gallery</span>
    <svg width="34" height="22" viewBox="0 0 34 22" aria-hidden="true">
      <circle cx="11" cy="11" r="9.5" fill="none" stroke="#111" stroke-width="1"/>
      <line x1="12" y1="11" x2="31" y2="11" stroke="var(--accent)" stroke-width="1.2"/>
      <polyline points="27,8 31,11 27,14" fill="none" stroke="var(--accent)" stroke-width="1.2"/>
    </svg>
  </a>

  <footer class="site-footer">©2022 Clara Wendt Art. All rights reserved.</footer>
</body>
</html>
```